Ridgeway Ore Advisory Business Card

Ridgeway Ore Advisory is a company that provides consulting services to the Mining Industry.

Whilst Ridgeway Ore Advisory is an Australian based company its client base is the global mining industry.

The essence of Ridgeway Ore Advisory is its a can do organisation that can make a difference to its clients by providing quality assistance and form lasting relationships.
Updates

Target Market(s)

The global Mining Industry.

Industry/Entity Type

Mining

Font styles to use
Serif

Colors

Designer to choose colors to be used in the design.

Requirements
Nice to have
• My thinking is the card would look good in black given the logo.

I would like to see written on the back side of the card " Providing Metallurgical, Management and Corporate Services to the Mining Industry"

```html
<!DOCTYPE html>
<html lang="en">
<head>
<meta charset="utf-8">
<title>Ridgeway Ore Advisory — Business Card</title>
<link rel="stylesheet" href="https://fonts.googleapis.com/css2?family=Open+Sans:wght@400;600;800&display=swap">
<style>
  :root {
    --backdrop: #e6e4e1;
    --card-dark: #07030c;
    --card-light: #ffffff;
    --accent-orange: #f3a21c;
    --ink: #1d1d1f;
    --ink-soft: #3a3a3c;
  }
  html, body {
    margin: 0;
    padding: 0;
    width: 1200px;
    height: 902px;
    overflow: hidden;
    background: var(--backdrop);
    font-family: "Open Sans", Arial, sans-serif;
  }
  .card-set {
    width: 1200px;
    height: 902px;
    display: flex;
    align-items: center;
    justify-content: center;
    gap: 60px;
  }
  .card {
    position: relative;
    width: 540px;
    height: 310px;
    box-sizing: border-box;
    box-shadow: 0 10px 28px rgba(0,0,0,0.18);
  }
  .card--front {
    background: var(--card-dark);
    display: flex;
    align-items: center;
    justify-content: center;
  }
  .brand-name {
    margin: 0;
    font-weight: 800;
    color: var(--accent-orange);
    letter-spacing: 0.5px;
    line-height: 1;
    text-transform: uppercase;
  }
  .card--front .brand-name { font-size: 24px; }
  .card--back {
    background: var(--card-light);
    display: flex;
    align-items: center;
    padding: 0 40px;
  }
  .card--back .brand-name {
    font-size: 15px;
    width: 190px;
    text-align: right;
  }
  .divider {
    width: 2px;
    height: 130px;
    background: var(--accent-orange);
    margin: 0 24px;
    flex-shrink: 0;
  }
  .contact { color: var(--ink-soft); }
  .contact__name {
    margin: 0;
    font-size: 24px;
    font-weight: 400;
    color: var(--ink);
    line-height: 1.1;
  }
  .contact__title {
    margin: 2px 0 12px;
    font-size: 13px;
  }
  .contact__list {
    list-style: none;
    margin: 0;
    padding: 0;
    font-size: 13px;
    line-height: 1.6;
  }
</style>
</head>
<body>
  <main class="card-set">
    <section class="card card--front" aria-label="Card front">
      <p class="brand-name">Ridgeway Ore Advisory</p>
    </section>

    <section class="card card--back" aria-label="Card back">
      <p class="brand-name">Ridgeway Ore Advisory</p>
      <div class="divider"></div>
      <div class="contact">
        <h1 class="contact__name">Name</h1>
        <p class="contact__title">Title</p>
        <ul class="contact__list">
          <li>xxx.xxx.xxxx</li>
          <li>email@email.com</li>
          <li>Adress</li>
          <li>www.web.com</li>
        </ul>
      </div>
    </section>
  </main>
</body>
</html>
```